Restaurant Business Card Template

I need a business card created in the same color scheme and style as the attached label. Preferably it'd be in a .ai format.

Industry/Entity Type

German Restaurant

Contact Information for Business Card

Verna Tollick, Front of House Manager, 312.774.2190, verna@brunfeldstuberestaurant.com, info@brunfeldstuberestaurant.com, 416 Birch Ave., Lower Level, Maplecrest, OR 97342.

Requirements
Must have
• Matching fonts and colors.
Nice to have
• If not able to match secondary font, something similar.

```html
<!DOCTYPE html>
<html lang="en">
<head>
<meta charset="utf-8">
<title>Brunfeldstube Restaurant – Business Card</title>
<link href="https://fonts.googleapis.com/css2?family=Lato:ital,wght@0,400;0,700;1,400&display=swap" rel="stylesheet">
<style>
  :root {
    --page: #ece9e3;
    --gold: #bba24f;
    --cream: #f3ead6;
    --cream-dark: #e7d9b9;
    --bavarian-blue: rgba(143,179,207,.85);
    --bavarian-fade: rgba(143,179,207,0);
    --ink: #2a2624;
    --ink-soft: #3d3733;
    --black-band: #231f20;
  }
  * { box-sizing: border-box; margin: 0; padding: 0; }
  html, body {
    width: 1200px; height: 900px; overflow: hidden;
    background: var(--page);
    font-family: "Lato", Arial, sans-serif;
    color: var(--ink);
  }
  .canvas { position: relative; width: 1200px; height: 900px; }
  .card {
    position: absolute; left: 320px;
    width: 560px; height: 320px;
    overflow: hidden;
    box-shadow: 0 6px 18px rgba(0,0,0,.18);
  }
  .card--front { top: 100px; background: var(--gold); }
  .card--back { top: 470px; background: linear-gradient(160deg, var(--cream) 0%, var(--cream-dark) 100%); }

  .brand {
    position: absolute; text-align: center;
    font-weight: 700; color: var(--ink);
    line-height: 1.1; letter-spacing: .5px;
  }
  .card--front .brand { left: 0; right: 0; top: 112px; font-size: 38px; }
  .card--back .brand { right: 30px; top: 38px; font-size: 24px; }

  .pattern-area {
    position: absolute; inset: 0;
    background: linear-gradient(150deg, var(--bavarian-blue) 0%, rgba(143,179,207,.4) 35%, var(--bavarian-fade) 62%);
  }

  .person { position: absolute; left: 50px; top: 42px; }
  .person__name { font-size: 22px; font-style: italic; color: var(--ink); }
  .person__title { font-size: 15px; color: var(--ink-soft); margin-top: 2px; }

  .address {
    position: absolute; left: 50px; top: 130px;
    font-size: 15px; line-height: 1.3; color: var(--ink);
  }
  .contacts {
    position: absolute; left: 50px; top: 180px;
    list-style: none; font-size: 14.5px; line-height: 1.45;
  }
  .contacts li { display: flex; align-items: center; gap: 8px; }
  .contacts svg { width: 13px; height: 11px; flex: none; }

  .swoosh { position: absolute; left: 0; bottom: 0; width: 560px; height: 320px; }
</style>
</head>
<body>
<main class="canvas">

  <section class="card card--front" aria-label="Card front">
    <p class="brand">Brunfeldstube<br>Restaurant</p>
  </section>

  <section class="card card--back" aria-label="Card back">
    <div class="pattern-area" role="img" aria-label="Faded blue and white Bavarian diamond pattern"></div>

    <p class="brand">Brunfeldstube<br>Restaurant</p>

    <div class="person">
      <p class="person__name">Verna Tollick</p>
      <p class="person__title">Front of House Manager</p>
    </div>

    <p class="address">416 Birch Ave., Lower Level<br>Maplecrest, OR 97342.</p>

    <ul class="contacts">
      <li>
        <svg viewBox="0 0 13 11" aria-hidden="true"><path d="M1 3 Q6.5 -1 12 3 L10 4.5 L9 3 H4 L3 4.5 Z M3 5 H10 L11.5 10 H1.5 Z" fill="var(--ink)"/></svg>
        312.774.2190
      </li>
      <li>
        <svg viewBox="0 0 13 11" aria-hidden="true"><rect x="0.5" y="1" width="12" height="9" fill="var(--ink)"/><path d="M1 1.5 L6.5 6 L12 1.5" stroke="var(--cream)" fill="none"/></svg>
        verna@brunfeldstuberestaurant.com
      </li>
      <li>
        <svg viewBox="0 0 13 11" aria-hidden="true"><rect x="0.5" y="1" width="12" height="9" fill="var(--ink)"/><path d="M1 1.5 L6.5 6 L12 1.5" stroke="var(--cream)" fill="none"/></svg>
        info@brunfeldstuberestaurant.com
      </li>
    </ul>

    <svg class="swoosh" viewBox="0 0 560 320" aria-hidden="true">
      <path d="M0 292 C180 288 300 238 400 200 C470 176 520 166 560 164 V320 H0 Z" fill="var(--gold)"/>
      <path d="M0 306 C180 302 300 254 405 218 C475 194 522 184 560 182 V320 H0 Z" fill="var(--black-band)"/>
    </svg>
  </section>

</main>
</body>
</html>
```